Varlow's Electrical & Solar - Business Cards

I want my business card to stand out from the rest. I will provide my business name logo and my icon logo to be implemented onto the card.

On the front of the card, can i have the following. Just make it neat & professional please.

Dean Harrop
varlowselectrical@mailbox-example.net
0491 837 562
ABN: 41 269 507 813
License No. 582146K
FREE QUOTES
24/7 Emergency

On the back of the card, can I have "Our Services" and maybe add the V logo on the back in the background or something. Under "Our Services" I want the following:

LED Lighting Upgrades
Switches & Outlets
Smoke Alarms
Switchboard Upgrades
Fault Finding
Rewiring
New Builds
Test & Tagging
All Electrical Maintenance & Repairs

Can you guys add the instagram logo and next to it, put varlows_electrical

Can you guys also add the facebook logo and next to it put Varlow's Electrical & Solar. Make sure the instagram & facebook icon is in either white, green or black.

Also I have put down double sided, not sure why when i save it, it keeps going to single sided. I need my business card double sided.

New Customers

Dean Harrop varlowselectrical@mailbox-example.net 0491 837 562 ABN: 41 269 507 813 License No. 582146K FREE QUOTES 24/7 Emergency

• must be tidy, professional and appealing

```html
<!DOCTYPE html>
<html lang="en">
<head>
<meta charset="utf-8">
<title>Varlow's Electrical &amp; Solar – Business Cards</title>
<link href="https://fonts.googleapis.com/css2?family=Exo+2:ital,wght@1,700;1,800;1,900&family=Russo+One&display=swap" rel="stylesheet">
<style>
  :root {
    --page: #1a1a1c;
    --card-dark: #070707;
    --card-mid: #1c1c1e;
    --card-light: #3a3a3d;
    --yellow: #ffc21a;
    --amber: #f39c1f;
    --orange: #e8692c;
    --coral: #e0564a;
    --white: #ffffff;
    --silver: #d4d6da;
    --silver-dark: #9a9ca1;
    --ink: #141414;
  }
  * { box-sizing: border-box; margin: 0; padding: 0; }
  html, body { width: 1200px; height: 900px; overflow: hidden; }
  body { background: var(--page); position: relative; font-family: "Exo 2", sans-serif; }

  .card {
    position: absolute; left: 230px; width: 740px; height: 410px; overflow: hidden;
    background: linear-gradient(100deg, var(--card-dark) 0%, var(--card-dark) 48%, var(--card-mid) 62%, var(--card-light) 100%);
    box-shadow: 0 10px 30px rgba(0,0,0,.6);
  }
  .card--back { top: 28px; }
  .card--front { top: 462px; }

  /* Back */
  .services-band {
    position: absolute; left: 0; top: 30px; width: 520px; height: 38px;
    background: linear-gradient(90deg, var(--orange) 0%, var(--amber) 35%, var(--yellow) 65%, rgba(255,194,26,0) 100%);
  }
  .services-title {
    position: absolute; left: 40px; top: 33px; font-family: "Russo One", sans-serif;
    font-size: 29px; letter-spacing: 1px; color: var(--ink); line-height: 34px;
  }
  .services-list { position: absolute; left: 42px; top: 80px; list-style: none; }
  .services-list li {
    position: relative; padding-left: 24px; color: var(--white);
    font-weight: 900; font-style: italic; font-size: 21px; line-height: 29px; letter-spacing: .5px;
  }
  .services-list li::before {
    content: ""; position: absolute; left: 0; top: 10px; width: 10px; height: 10px;
    border-radius: 50%; background: var(--amber);
  }
  .services-list li.continued { padding-left: 10px; }
  .services-list li.continued::before { display: none; }

  .brand-mark {
    position: absolute; left: 545px; top: 60px; width: 150px; height: 150px; border-radius: 50%;
    border: 7px solid var(--amber); display: flex; align-items: center; justify-content: center;
    font-family: "Russo One", sans-serif; font-size: 24px; color: var(--silver);
  }
  .social { position: absolute; left: 440px; top: 350px; display: flex; align-items: center; gap: 12px; }
  .social-square { width: 24px; height: 24px; border-radius: 4px; background: var(--amber); }
  .social-handle { color: var(--white); font-weight: 900; font-style: italic; font-size: 23px; letter-spacing: .5px; }

  /* Front */
  .wordmark {
    position: absolute; right: 50px; top: 52px; text-align: center;
    font-family: "Russo One", sans-serif; color: var(--silver);
  }
  .wordmark-name { font-size: 58px; line-height: 62px; letter-spacing: 1px; }
  .wordmark-tag { font-size: 17px; letter-spacing: 6px; line-height: 22px; }

  .holder-name {
    position: absolute; left: 40px; top: 175px; font-family: "Russo One", sans-serif;
    font-size: 33px; letter-spacing: 2px; color: var(--amber);
  }
  .holder-rule { position: absolute; left: 36px; top: 222px; width: 480px; height: 2px; background: var(--silver-dark); }
  .free-quotes {
    position: absolute; left: 500px; top: 228px; width: 220px; height: 46px;
    background: linear-gradient(90deg, var(--silver-dark), var(--silver));
    display: flex; align-items: center; justify-content: center;
    font-weight: 900; font-style: italic; font-size: 23px; letter-spacing: 1px; color: var(--ink);
  }
  .contact { position: absolute; left: 40px; list-style: none; }
  .contact--phone { top: 262px; }
  .contact--email { top: 300px; }
  .contact li { display: flex; align-items: center; gap: 12px; color: var(--white); font-weight: 800; font-style: italic; }
  .contact--phone li { font-size: 25px; letter-spacing: 1px; }
  .contact--email li { font-size: 20px; }
  .contact-icon { width: 26px; height: 26px; flex: none; }

  .emergency { position: absolute; left: 520px; top: 282px; width: 200px; height: 80px; }

  .legal-band {
    position: absolute; left: 0; bottom: 0; width: 100%; height: 52px;
    border-top: 3px solid var(--silver-dark);
    background: linear-gradient(90deg, var(--yellow) 0%, var(--amber) 45%, var(--orange) 80%, var(--coral) 100%);
    display: flex; align-items: center; padding-left: 40px;
    font-weight: 900; font-style: italic; font-size: 21px; letter-spacing: 1px; color: var(--ink);
  }
</style>
</head>
<body>

<section class="card card--back" aria-label="Card back – services">
  <div class="services-band"></div>
  <h2 class="services-title">OUR SERVICES</h2>
  <ul class="services-list">
    <li>LED Lighting Upgrades</li>
    <li>Switches &amp; Outlets</li>
    <li>Smoke Alarms</li>
    <li>Switchboard Upgrades</li>
    <li>Fault Finding</li>
    <li>Rewiring</li>
    <li>New Builds</li>
    <li>Test &amp; Tagging</li>
    <li>All Electrical</li>
    <li class="continued">Maintenance &amp; Repairs</li>
  </ul>
  <div class="brand-mark">VARLOW'S</div>
  <div class="social">
    <span class="social-square" aria-hidden="true"></span>
    <span class="social-handle">varlows_electrical</span>
  </div>
</section>

<section class="card card--front" aria-label="Card front – contact details">
  <div class="wordmark">
    <div class="wordmark-name">VARLOW'S</div>
    <div class="wordmark-tag">ELECTRICAL &amp; SOLAR</div>
  </div>

  <h1 class="holder-name">DEAN HARROP</h1>
  <div class="holder-rule"></div>
  <div class="free-quotes">FREE QUOTES</div>

  <ul class="contact contact--phone">
    <li>
      <svg class="contact-icon" viewBox="0 0 26 26" aria-hidden="true">
        <circle cx="13" cy="13" r="13" fill="#f39c1f"/>
        <path d="M9 7.5c.6-.4 1.3-.3 1.7.3l1.2 2c.3.5.2 1.1-.2 1.5l-.8.7c.6 1.4 1.7 2.5 3.1 3.1l.7-.8c.4-.4 1-.5 1.5-.2l2 1.2c.6.4.7 1.1.3 1.7l-.8 1c-.6.7-1.6.9-2.5.5-3-1.3-5.4-3.7-6.7-6.7-.4-.9-.2-1.9.5-2.5z" fill="#141414"/>
      </svg>
      0491 837 562
    </li>
  </ul>
  <ul class="contact contact--email">
    <li>
      <svg class="contact-icon" viewBox="0 0 26 26" aria-hidden="true">
        <circle cx="13" cy="13" r="13" fill="#f39c1f"/>
        <rect x="6.5" y="8.5" width="13" height="9" rx="1" fill="none" stroke="#141414" stroke-width="1.6"/>
        <path d="M6.8 9l6.2 5 6.2-5" fill="none" stroke="#141414" stroke-width="1.6"/>
      </svg>
      varlowselectrical@mailbox-example.net
    </li>
  </ul>

  <svg class="emergency" viewBox="0 0 200 80" aria-label="24/7 Emergency">
    <path d="M30 62 A30 30 0 1 1 78 18" fill="none" stroke="#e0564a" stroke-width="4"/>
    <path d="M70 6 L92 18 L70 28 Z" fill="#f39c1f"/>
    <text x="20" y="48" font-family="Russo One, sans-serif" font-size="26" fill="#d4d6da">24/7</text>
    <path d="M82 32 H186 L194 42 L186 52 H82 Z" fill="#ffc21a"/>
    <text x="90" y="48" font-family="Exo 2, sans-serif" font-style="italic" font-weight="900" font-size="15" fill="#141414">EMERGENCY</text>
  </svg>

  <div class="legal-band">ABN: 41 269 507 813 // License No. 582146K</div>
</section>

</body>
</html>
```